Indie Comedy Film Needs Kick Ass Movie Poster

Our film "Velvet Harbor Patrol" is an over-the-top comedy in the vein of "Maple Hollow". It is a live action comedy satire musical, all-in-one!

Synopsis: A group of mysterious villains known as ‘The Syndicate’ sets a trap for the Taxpayer. They imprison him, torture him, and make plans to publicly crucify him. Local janitor Gordon Whitlock rounds up retired Superheroes, and hatches a plan to rescue the Taxpayer. The villains stage a public rally, where many citizens come to watch the Taxpayer’s crucifixion. The heroes invade the bad guy lair, and a large battle ensues. Various comedic and action-packed musical numbers are intertwined throughout the madness. In the midst of the big political debate and battle for mankind will the heroes save the day?

A Trailer can be viewed here:
https://www.clipvault-example.net/watch?v=qpLzTRa7Xnu

We are looking for a one sheet poster design that stresses the action comedy element of the film. We have attached some photos of the design from the older Loose Cannon movies which went in the same direction. Same with the recent "Mud Pie". We would like to have the poster contain some kind of US Patriotic theme (think fireworks, red white and blue, bald eagles, stars and stripes, perhaps the Statue of Liberty, etc.The theme does not necessarily have to "hit you over the head", so would be interested in seeing ideas that cover a spectrum. Many photo elements from the film are also attached below. Give it your best shot!
Updates

Thank you all for your great designs! We are currently reviewing, and will be picking a top design (or perhaps two) in the next few days

Target Market(s)

Men and women ages 15-45. US Audience.

Industry/Entity Type

Political

Colors

Designer to choose colors to be used in the design.

Requirements
Must have
• We would like to have the poster contain some kind of US Patriotic theme (think fireworks, red white and blue, bald eagles, stars and stripes, perhaps the Statue of Liberty, etc.The theme does not necessarily have to "hit you over the head", so would be interested in seeing ideas that cover a spectrum.
Nice to have
• A tagline that can be used is "Fresh Out of Retirement...They Don't Stand a Chance" or try your own!

```html
<!DOCTYPE html>
<html lang="en">
<head>
<meta charset="utf-8">
<title>Velvet Harbor Patrol — One Sheet</title>
<link href="https://fonts.googleapis.com/css2?family=Bebas+Neue&family=Oswald:wght@500;700&display=swap" rel="stylesheet">
<style>
  :root {
    --sky-top: #dfe9f3;
    --sky-mid: #f4f6f9;
    --ray-red: #d9485a;
    --ray-soft: #e57a86;
    --navy: #1b3f78;
    --blue: #2f66b0;
    --purple: #5a3f7a;
    --crimson: #c3203a;
    --red: #e02c3b;
    --ink: #232330;
    --white: #ffffff;
    --ground: #b9505c;
    --cast-visor: #2c4756;
    --cast-janitor: #7b6a78;
    --cast-boxer: #5e6068;
    --cast-caped: #3d5fa8;
  }
  * { margin: 0; padding: 0; box-sizing: border-box; }
  html, body { width: 801px; height: 1200px; overflow: hidden; background: var(--sky-mid); }
  .poster {
    position: relative;
    width: 801px;
    height: 1200px;
    overflow: hidden;
    background: linear-gradient(180deg, var(--sky-top) 0%, var(--sky-mid) 45%, #f1e3e6 62%, #d98b94 82%, var(--ground) 100%);
    font-family: "Bebas Neue", "Oswald", sans-serif;
    color: var(--ink);
  }
  .rays { position: absolute; inset: 0; }
  .tagline {
    position: absolute;
    top: 36px; left: 0; width: 100%;
    text-align: center;
    font-size: 27px;
    line-height: 1;
    letter-spacing: 0.5px;
    color: var(--ink);
  }
  .cast { position: absolute; inset: 0; }
  .cast-member {
    position: absolute;
    border-radius: 70px 70px 0 0;
  }
  .cast-member.hero-visor { left: 0; top: 82px; width: 168px; height: 560px;
    background: linear-gradient(180deg, var(--cast-visor) 0%, var(--cast-visor) 60%, rgba(44,71,86,0) 100%);
    border-radius: 0 70px 0 0; }
  .cast-member.hero-janitor { left: 186px; top: 130px; width: 222px; height: 520px;
    background: linear-gradient(180deg, var(--cast-janitor) 0%, var(--cast-janitor) 60%, rgba(123,106,120,0) 100%); }
  .cast-member.hero-boxer { left: 398px; top: 128px; width: 222px; height: 520px;
    background: linear-gradient(180deg, var(--cast-boxer) 0%, var(--cast-boxer) 60%, rgba(94,96,104,0) 100%); }
  .cast-member.hero-caped { left: 638px; top: 80px; width: 163px; height: 560px;
    background: linear-gradient(180deg, var(--cast-caped) 0%, var(--cast-caped) 60%, rgba(61,95,168,0) 100%);
    border-radius: 70px 0 0 0; }
  .title {
    position: absolute;
    left: 0; width: 100%;
    text-align: center;
    font-family: "Bebas Neue", sans-serif;
    font-weight: 400;
    line-height: 0.85;
    background: linear-gradient(90deg, var(--navy) 0%, var(--blue) 30%, var(--purple) 55%, var(--crimson) 78%, var(--red) 100%);
    -webkit-background-clip: text;
    background-clip: text;
    color: transparent;
    filter:
      drop-shadow(2px 0 0 var(--white)) drop-shadow(-2px 0 0 var(--white))
      drop-shadow(0 2px 0 var(--white)) drop-shadow(0 -2px 0 var(--white))
      drop-shadow(0 3px 2px rgba(20,20,40,0.5));
    white-space: nowrap;
  }
  .title-top { top: 606px; font-size: 148px; letter-spacing: 0; }
  .title-main { top: 730px; font-size: 338px; letter-spacing: 2px; }
  .billing {
    position: absolute;
    left: 40px; right: 40px; top: 1084px;
    color: var(--ink);
    white-space: nowrap;
  }
  .billing-line { display: flex; align-items: center; gap: 8px; height: 28px; font-size: 21px; }
  .label {
    display: inline-block;
    font-family: "Oswald", sans-serif;
    font-weight: 500;
    font-size: 7px;
    line-height: 1.05;
    text-align: right;
    text-transform: uppercase;
  }
  .small { font-family: "Oswald", sans-serif; font-weight: 500; font-size: 9px; text-transform: uppercase; }
</style>
</head>
<body>
<main class="poster">
  <svg class="rays" viewBox="0 0 801 1200" width="801" height="1200" aria-hidden="true">
    <g fill="var(--ray-red)" opacity="0.75">
      <polygon points="400,1300 -120,0 40,0"/>
      <polygon points="400,1300 200,0 300,0"/>
      <polygon points="400,1300 500,0 600,0"/>
      <polygon points="400,1300 760,0 920,0"/>
      <polygon points="400,1300 -400,380 -400,700"/>
      <polygon points="400,1300 1200,380 1200,700"/>
    </g>
    <g fill="var(--ray-soft)" opacity="0.25">
      <polygon points="400,1300 40,0 200,0"/>
      <polygon points="400,1300 600,0 760,0"/>
    </g>
  </svg>

  <p class="tagline">Fresh out of retirement...They don't stand a chance</p>

  <section class="cast">
    <div class="cast-member hero-visor" role="img" aria-label="Hero in visor and black coat holding a sword"></div>
    <div class="cast-member hero-janitor" role="img" aria-label="Janitor hero with cape, arms crossed, stained t-shirt"></div>
    <div class="cast-member hero-boxer" role="img" aria-label="Hero in aviator sunglasses and boxing gloves, arms crossed"></div>
    <div class="cast-member hero-caped" role="img" aria-label="Caped hero in blue suit with red tights, hands on hips"></div>
  </section>

  <h1>
    <span class="title title-top">Velvet Harbor</span>
    <span class="title title-main">Patrol</span>
  </h1>

  <footer class="billing">
    <div class="billing-line">Studio Name Pictures <span class="small">presents a</span> Producers <span class="small">a film by</span> Script Writer Actor One Actor Two “Movie Title”</div>
    <div class="billing-line"><span class="label">Music<br>by</span> The Musician <span class="label">Costume<br>designer</span> Designer Name <span class="label">Edited<br>by</span> Editors Name <span class="label">Production<br>designer</span> Designers Name <span class="label">Director of<br>photography</span> Cinematographer</div>
    <div class="billing-line"><span class="label">Executive<br>producer</span> Ex Producer 1 Ex Producer 2 <span class="label">Produced<br>by</span> Producer One Producer 2 <span class="label">Story<br>by</span> Story Writer</div>
    <div class="billing-line"><span class="label">Screenplay<br>by</span> Screen Writer <span class="label">Directed<br>by</span> Director Name</div>
  </footer>
</main>
</body>
</html>
```